Need a business card created for my Heating and Air-conditioning business

We are a new Air Conditioning , Refrigeration and Heating business called Frost & Cinder HVAC/R - we do repairs, maintenance and installations.

Our motto is "Skilled Precision - Superior Value"

Information needed on the card:
Leon Marsh
604-555-0187
www.frosthvac.example
info@frosthvac.example

```html
<!DOCTYPE html>
<html lang="en">
<head>
<meta charset="utf-8">
<title>Frost &amp; Cinder HVAC/R — Business Card</title>
<link rel="stylesheet" href="https://fonts.googleapis.com/css2?family=Montserrat:wght@500&display=swap">
<style>
  :root {
    --navy: #14104a;
    --red: #c8182a;
    --paper: #f4f3f0;
    --backdrop: #d9d9d9;
    --ice: #a9c8e4;
    --white: #ffffff;
  }
  html, body {
    margin: 0;
    width: 1200px;
    height: 1200px;
    overflow: hidden;
    background: var(--backdrop);
    font-family: "Montserrat", sans-serif;
  }
  .card {
    position: absolute;
    left: 250px;
    width: 700px;
    height: 400px;
    box-shadow: 0 6px 18px rgba(0,0,0,.18);
    overflow: hidden;
  }
  .card-front {
    top: 150px;
    background: var(--navy);
    color: var(--white);
    display: flex;
    align-items: center;
    justify-content: center;
  }
  .brand {
    display: flex;
    align-items: center;
    gap: 22px;
  }
  .brand-dot {
    width: 22px;
    height: 22px;
    border-radius: 50%;
    background: var(--ice);
  }
  .brand-name {
    font-size: 40px;
    font-weight: 500;
    letter-spacing: 2px;
    line-height: 1.25;
  }
  .card-back {
    top: 650px;
    background: var(--paper);
  }
  .accent-panel {
    position: absolute;
    left: 0;
    top: 0;
  }
  .panel-brand {
    position: absolute;
    left: 44px;
    top: 130px;
    width: 190px;
    color: var(--white);
    font-size: 28px;
    font-weight: 500;
    letter-spacing: 1px;
    line-height: 1.3;
  }
  .contact {
    position: absolute;
    left: 360px;
    top: 95px;
    color: var(--navy);
  }
  .contact-name {
    margin: 0 0 26px;
    font-size: 40px;
    font-weight: 500;
    letter-spacing: 1px;
    text-transform: uppercase;
  }
  .contact-list {
    list-style: none;
    margin: 0;
    padding: 0;
    font-size: 22px;
    font-weight: 500;
  }
  .contact-list li {
    display: flex;
    align-items: center;
    gap: 14px;
    margin-bottom: 16px;
  }
  .contact-list svg {
    width: 22px;
    height: 22px;
    flex: none;
  }
</style>
</head>
<body>

<section class="card card-front">
  <div class="brand">
    <span class="brand-dot"></span>
    <div class="brand-name">Frost &amp; Cinder<br>HVAC/R</div>
  </div>
</section>

<section class="card card-back">
  <svg class="accent-panel" width="700" height="400" viewBox="0 0 700 400" aria-hidden="true">
    <path d="M0 0 H200 C205 80 330 110 322 220 C314 320 205 340 170 400 H0 Z" fill="var(--red)"/>
  </svg>
  <div class="panel-brand">Frost &amp; Cinder HVAC/R</div>

  <div class="contact">
    <h1 class="contact-name">Leon Marsh</h1>
    <ul class="contact-list">
      <li>
        <svg viewBox="0 0 24 24" aria-hidden="true"><circle cx="12" cy="12" r="10" fill="none" stroke="var(--red)" stroke-width="2"/><path d="M8.5 7.5c.6-.6 1.4-.4 1.7.2l.8 1.6c.2.5 0 1-.4 1.3l-.6.4c.6 1.3 1.6 2.3 2.9 2.9l.4-.6c.3-.4.8-.6 1.3-.4l1.6.8c.6.3.8 1.1.2 1.7-1.6 1.6-4 .6-6-1.4s-3-4.4-1.9-6.5z" fill="var(--red)"/></svg>
        604-555-0187
      </li>
      <li>
        <svg viewBox="0 0 24 24" aria-hidden="true"><circle cx="12" cy="12" r="10" fill="var(--red)"/><path d="M2 12h20M12 2c3 3 3 17 0 20M12 2c-3 3-3 17 0 20" fill="none" stroke="var(--paper)" stroke-width="1.5"/></svg>
        www.frosthvac.example
      </li>
      <li>
        <svg viewBox="0 0 24 24" aria-hidden="true"><rect x="2" y="5" width="20" height="14" fill="var(--red)"/><path d="M2 5l10 8 10-8" fill="none" stroke="var(--paper)" stroke-width="1.5"/></svg>
        info@frosthvac.example
      </li>
    </ul>
  </div>
</section>

</body>
</html>
```